App für weniger Konsum
Zielgruppe
Wir sind ein Startup, das Nutzer:innen in einem bewussteren Kaufverhalten stärkt. Dabei werden Nutzer:innen psychologischen Kaufprofilen zugeordnet und individuell auf dem Weg begleitet, weniger einzukaufen. Das stärkt die Finanzen und schützt die Umwelt.
Aufgabenstellung
Das Design sollte einerseits minimalismusorientierte Nutzer:innen ansprechen (clean, ruhig), aber auch Nutzer:innen ansprechen, die sich noch nicht mit weniger / besserem Konsum beschäftigt haben.
Es wäre toll folgende Slides zu haben:
- Anmeldung / Registrierung
- Quiz (Es soll direkt zu Beginn ein Quiz aus mehreren Slides geben, das Nutzer:innen einem Kauftypen zuordnet(
- Quizergebnis (Du bist Kauftyp XYZ...)
- Home-Screen der App / Navigation
- Statistiken: Du hast diesen Monat so viel gespart...
- Slide mit Einstellungen
- 'Challenge' Slide: 10 tage aussortieren

```html
<!DOCTYPE html>
<html lang="de">
<head>
<meta charset="utf-8">
<title>Kaufstil App – Screens</title>
<link href="https://fonts.googleapis.com/css2?family=Inter:wght@400;500;600;700&display=swap" rel="stylesheet">
<style>
:root{
  --canvas:#3d3d3d;
  --screen:#0a0a0a;
  --frame:#1c1c1c;
  --card:#151515;
  --card-line:#232323;
  --text:#ffffff;
  --muted:#8a8a8a;
  --dim:#5e5e5e;
  --label:#9a9a9a;
  --lime:#c5f25b;
  --purple:#7b6cf0;
  --danger:#e5533f;
}
*{box-sizing:border-box;margin:0;padding:0}
html,body{width:1200px;height:4451px;overflow:hidden}
body{background:var(--canvas);font-family:'Inter',sans-serif;color:var(--text);position:relative}
svg{display:block}
.screen-label{position:absolute;width:339px;text-align:center;font-size:11px;letter-spacing:1.3px;color:var(--label);text-transform:uppercase}
.phone{position:absolute;width:339px;height:788px;border-radius:40px;background:linear-gradient(180deg,#121212 0%,var(--screen) 30%);border:5px solid var(--frame);overflow:hidden;box-shadow:0 0 0 1px #2a2a2a}
.abs{position:absolute}
.center{left:0;right:0;text-align:center}
.title{font-weight:400;letter-spacing:-.4px}
.progress{position:absolute;top:0;left:28px;right:28px;height:3px;background:#1b1b1b}
.progress span{display:block;height:3px;background:var(--lime)}
.kicker{position:absolute;left:33px;top:68px;font-size:11px;font-weight:600;letter-spacing:1px;color:var(--lime)}
.question{position:absolute;left:33px;right:28px;top:87px;font-size:22px;line-height:31px;font-weight:400;letter-spacing:-.3px}
.option{position:absolute;left:33px;width:263px;background:var(--card);border:1px solid var(--card-line);border-radius:16px;padding:22px 48px 18px 22px}
.option h3{font-size:16px;font-weight:500;line-height:24px}
.option p{font-size:12px;line-height:18px;color:var(--dim);margin-top:6px}
.option svg{position:absolute;right:20px;top:24px;color:#777}
.next{position:absolute;left:250px;width:52px;height:52px;border-radius:50%;background:var(--lime);color:#000;display:flex;align-items:center;justify-content:center}
.btn{position:absolute;left:33px;width:263px;height:50px;border-radius:25px;display:flex;align-items:center;justify-content:center;font-size:15px;font-weight:500}
.btn-white{background:#fff;color:#000}
.btn-dark{background:#161616;border:1px solid #262626;color:#fff}
.btn-lime{background:var(--lime);color:#0a0a0a}
.round-icon{position:absolute;width:36px;height:36px;border-radius:50%;background:#1a1a1a;border:1px solid #2a2a2a;display:flex;align-items:center;justify-content:center;color:#ccc}
.nav{position:absolute;left:0;right:0;bottom:0;height:88px;border-top:1px solid #1e1e1e;background:#0c0c0c;display:flex;justify-content:space-around;padding-top:20px}
.nav-item{display:flex;flex-direction:column;align-items:center;gap:8px;font-size:9px;color:var(--dim);width:60px}
.nav-item svg{color:#777}
.nav-item.active,.nav-item.active svg{color:var(--lime)}
.section-title{position:absolute;left:33px;font-size:10.5px;letter-spacing:1.3px;color:var(--dim);font-weight:500}
.group{position:absolute;left:33px;width:263px;background:var(--card);border:1px solid var(--card-line);border-radius:14px;overflow:hidden}
.row{height:53px;display:flex;align-items:center;justify-content:space-between;padding:0 16px;font-size:14px;border-top:1px solid #1f1f1f;color:#eee}
.row:first-child{border-top:none}
.row .meta{color:var(--muted);font-size:12px}
.row svg{color:#666}
.toggle{width:40px;height:22px;border-radius:11px;background:var(--lime);position:relative}
.toggle::after{content:"";position:absolute;right:3px;top:3px;width:16px;height:16px;border-radius:50%;background:#0a0a0a}
.profile-card{position:absolute;left:33px;width:263px;background:var(--card);border:1px solid var(--card-line);border-radius:16px;padding:24px 22px}
.profile-card .badge{width:32px;height:32px;border-radius:50%;display:flex;align-items:center;justify-content:center;margin-bottom:18px}
.profile-card h3{font-size:16px;font-weight:500;margin-bottom:10px}
.profile-card p{font-size:12px;line-height:21px;color:var(--muted)}
.stat-box{position:absolute;top:415px;width:123px;height:135px;background:var(--card);border:1px solid var(--card-line);border-radius:14px;padding:16px 16px}
.stat-box strong{display:block;font-size:22px;font-weight:600;margin-top:14px}
.stat-box span{display:block;font-size:10px;line-height:14px;color:var(--dim);margin-top:4px}
.win-card{position:absolute;left:33px;width:263px;background:var(--card);border:1px solid var(--card-line);border-radius:14px;padding:18px 16px 16px 68px}
.win-card .badge{position:absolute;left:18px;top:18px;width:34px;height:34px;border-radius:50%;display:flex;align-items:center;justify-content:center}
.win-card h4{font-size:14px;font-weight:500;line-height:20px}
.win-card p{font-size:11.5px;line-height:18px;color:var(--muted);margin-top:4px}
.step{position:absolute;left:50px;font-size:12.5px;color:#ddd;display:flex;align-items:center;gap:26px}
.step::before{content:"";width:8px;height:8px;border-radius:50%;background:#444}
</style>
</head>
<body>

<div class="screen-label" style="left:45px;top:45px">1. Login &amp; Registrierung</div>
<div class="screen-label" style="left:430px;top:45px">2. Quiz Intro</div>
<div class="screen-label" style="left:814px;top:45px">3. Quiz Question 1</div>

<!-- 1 Login -->
<section class="phone" style="left:45px;top:76px">
  <div class="abs" style="left:144px;top:97px;width:41px;height:41px;border-radius:11px;background:#1e2615;border:1px solid #2d3a1c"></div>
  <h1 class="abs center title" style="top:165px;font-size:28px">Willkommen zurück</h1>
  <p class="abs center" style="top:208px;font-size:14.5px;line-height:22px;color:var(--muted);padding:0 40px">Dein Begleiter für bewusstes Konsumieren.</p>
  <div class="btn btn-white" style="top:287px">Mit Nordkonto anmelden</div>
  <div class="btn btn-dark" style="top:353px">Mit Lumenkonto anmelden</div>
  <div class="abs" style="left:33px;right:38px;top:448px;display:flex;align-items:center;gap:10px;font-size:10.5px;letter-spacing:1.3px;color:var(--dim)">
    <span style="flex:1;height:1px;background:#222"></span>ODER MIT EMAIL<span style="flex:1;height:1px;background:#222"></span>
  </div>
  <label class="abs" style="left:33px;top:497px;font-size:11px;color:#bbb">Email Adresse</label>
  <div class="abs" style="left:33px;top:514px;width:263px;height:48px;border-radius:12px;background:#141414;border:1px solid #262626"></div>
  <div class="btn btn-lime" style="top:580px">Weiter</div>
  <p class="abs center" style="top:734px;font-size:10px;color:#555">Mit der Anmeldung akzeptierst du unsere <u>AGB</u>.</p>
</section>

<!-- 2 Quiz intro -->
<section class="phone" style="left:430px;top:76px">
  <div class="round-icon" style="left:32px;top:46px">
    <svg width="14" height="14" viewBox="0 0 24 24" fill="none" stroke="currentColor" stroke-width="2.2" stroke-linecap="round"><path d="M6 6l12 12M18 6L6 18"/></svg>
  </div>
  <div class="abs" style="left:104px;top:115px;width:121px;height:121px;border-radius:50%;background:radial-gradient(circle,#2c3a1d 0%,#1a2213 70%);display:flex;align-items:center;justify-content:center;color:var(--lime)">
    <svg width="44" height="44" viewBox="0 0 24 24" fill="none" stroke="currentColor" stroke-width="1.6" stroke-linejoin="round"><path d="M10 3l1.8 5.2L17 10l-5.2 1.8L10 17l-1.8-5.2L3 10l5.2-1.8z"/><path d="M18 14l.8 2.2L21 17l-2.2.8L18 20l-.8-2.2L15 17l2.2-.8z"/></svg>
  </div>
  <h1 class="abs center title" style="top:278px;font-size:29px;line-height:35px">Lerne deinen<br>Kaufstil kennen</h1>
  <p class="abs center" style="top:362px;font-size:15.5px;line-height:27.5px;color:var(--muted);padding:0 54px">Dieses kurze Quiz hilft uns zu verstehen, was deine Kaufentscheidungen antreibt. Es gibt keine falschen Antworten – nur Erkenntnisse.</p>
  <div class="abs" style="left:47px;top:553px;width:233px;height:97px;border-radius:14px;background:#141414;border:1px solid #222;padding:22px 20px;font-size:11.5px;color:#777;display:flex;flex-direction:column;gap:16px">
    <div style="display:flex;gap:10px;align-items:center"><svg width="14" height="14" viewBox="0 0 24 24" fill="none" stroke="var(--lime)" stroke-width="2"><circle cx="12" cy="12" r="9"/><path d="M12 7v5l3 2"/></svg>Dauer: ca. 2 Minuten</div>
    <div style="display:flex;gap:10px;align-items:center"><svg width="14" height="14" viewBox="0 0 24 24" fill="none" stroke="var(--lime)" stroke-width="2"><path d="M12 3l8 3v6c0 5-4 8-8 9-4-1-8-4-8-9V6z"/><path d="M9 12l2 2 4-4"/></svg>Daten bleiben privat</div>
  </div>
  <div class="btn btn-white" style="top:688px;left:31px;width:265px;height:59px;border-radius:30px;justify-content:space-between;padding:0 28px;font-size:15px">Starten
    <svg width="16" height="16" viewBox="0 0 24 24" fill="none" stroke="currentColor" stroke-width="2" stroke-linecap="round"><path d="M5 12h14M13 6l6 6-6 6"/></svg></div>
</section>

<!-- 3 Quiz Q1 -->
<section class="phone" style="left:814px;top:76px">
  <div class="progress"><span style="width:20%"></span></div>
  <div class="kicker">SITUATION 01/05</div>
  <h2 class="question">Du betrittst ein Geschäft. Wohin geht dein erster Blick?</h2>
  <div class="option" style="top:266px;height:114px"><h3>Zur Sale-Abteilung</h3><p>Ich liebe es, Schnäppchen zu finden.</p>
    <svg width="16" height="16" viewBox="0 0 24 24" fill="none" stroke="currentColor" stroke-width="2" stroke-linecap="round"><path d="M19 5L5 19"/><circle cx="7" cy="7" r="2"/><circle cx="17" cy="17" r="2"/></svg></div>
  <div class="option" style="top:400px;height:114px"><h3>Zu den Neuheiten</h3><p>Ich möchte wissen, was im Trend liegt.</p>
    <svg width="16" height="16" viewBox="0 0 24 24" fill="none" stroke="currentColor" stroke-width="1.8" stroke-linejoin="round"><path d="M10 3l1.8 5.2L17 10l-5.2 1.8L10 17l-1.8-5.2L3 10l5.2-1.8z"/><path d="M18 14l.8 2.2L21 17l-2.2.8L18 20l-.8-2.2L15 17l2.2-.8z"/></svg></div>
  <div class="option" style="top:533px;height:97px"><h3>Gezielt zum Produkt</h3><p>Ich hole nur, was ich brauche.</p>
    <svg width="16" height="16" viewBox="0 0 24 24" fill="none" stroke="currentColor" stroke-width="2"><circle cx="12" cy="12" r="9"/><circle cx="12" cy="12" r="5"/><circle cx="12" cy="12" r="1"/></svg></div>
  <div class="next" style="top:695px"><svg width="18" height="18" viewBox="0 0 24 24" fill="none" stroke="currentColor" stroke-width="2.2" stroke-linecap="round"><path d="M5 12h14M13 6l6 6-6 6"/></svg></div>
</section>

<div class="screen-label" style="left:45px;top:912px">4. Quiz Question 2</div>
<div class="screen-label" style="left:430px;top:912px">5. Quiz Question 3</div>
<div class="screen-label" style="left:814px;top:912px">6. Quiz Question 4</div>

<!-- 4 Quiz Q2 -->
<section class="phone" style="left:45px;top:942px">
  <div class="progress"><span style="width:40%"></span></div>
  <div class="kicker">SITUATION 02/05</div>
  <h2 class="question">Ein stressiger Tag geht zu Ende. Du siehst eine Werbung für etwas, das du magst. Was fühlst du?</h2>
  <div class="option" style="top:258px;height:142px"><h3>Ich verdiene eine Belohnung</h3><p>Der Kauf würde mir sofort gute Laune machen.</p>
    <svg width="16" height="16" viewBox="0 0 24 24" fill="none" stroke="currentColor" stroke-width="2"><rect x="4" y="9" width="16" height="11" rx="1"/><path d="M3 9h18M12 9v11M12 9c-2-4-6-4-6-1s6 1 6 1c2-4 6-4 6-1s-6 1-6 1"/></svg></div>
  <div class="option" style="top:419px;height:114px"><h3>Gleichgültigkeit</h3><p>Ich scrolle weiter, es berührt mich heute nicht.</p>
    <svg width="16" height="16" viewBox="0 0 24 24" fill="none" stroke="currentColor" stroke-width="2" stroke-linecap="round"><circle cx="12" cy="12" r="9"/><path d="M9 15h6M9 10h.01M15 10h.01"/></svg></div>
  <div class="option" style="top:553px;height:116px"><h3>Kaufdruck</h3><p>Ich habe Angst, ein gutes Angebot zu verpassen.</p>
    <svg width="16" height="16" viewBox="0 0 24 24" fill="none" stroke="currentColor" stroke-width="2" stroke-linecap="round"><circle cx="12" cy="12" r="9"/><path d="M12 8v5M12 16h.01"/></svg></div>
  <div class="next" style="top:697px"><svg width="18" height="18" viewBox="0 0 24 24" fill="none" stroke="currentColor" stroke-width="2.2" stroke-linecap="round"><path d="M5 12h14M13 6l6 6-6 6"/></svg></div>
</section>

<!-- 5 Quiz Q3 -->
<section class="phone" style="left:430px;top:942px">
  <div class="progress"><span style="width:60%"></span></div>
  <div class="kicker">SITUATION 03/05</div>
  <h2 class="question">Ein Online-Warenkorb ist voll. Was tust du?</h2>
  <div class="option" style="top:268px;height:100px"><h3>Sofort bestellen</h3><p>Bevor es ausverkauft ist.</p>
    <svg width="16" height="16" viewBox="0 0 24 24" fill="none" stroke="currentColor" stroke-width="2"><rect x="3" y="6" width="18" height="13" rx="2"/><path d="M3 10h18"/></svg></div>
  <div class="option" style="top:384px;height:99px"><h3>Erstmal liegen lassen</h3><p>Ich schlafe eine Nacht darüber.</p>
    <svg width="16" height="16" viewBox="0 0 24 24" fill="none" stroke="currentColor" stroke-width="2"><circle cx="12" cy="12" r="9"/><path d="M12 7v5l3 2"/></svg></div>
  <div class="option" style="top:500px;height:95px"><h3>Aussortieren</h3><p>Ich reduziere auf das Nötigste.</p>
    <svg width="16" height="16" viewBox="0 0 24 24" fill="none" stroke="currentColor" stroke-width="2" stroke-linecap="round"><path d="M4 7h16M9 7V4h6v3M6 7l1 13h10l1-13M10 11v6M14 11v6"/></svg></div>
  <div class="next" style="top:697px"><svg width="18" height="18" viewBox="0 0 24 24" fill="none" stroke="currentColor" stroke-width="2.2" stroke-linecap="round"><path d="M5 12h14M13 6l6 6-6 6"/></svg></div>
</section>

<!-- 6 Quiz Q4 -->
<section class="phone" style="left:814px;top:942px">
  <div class="progress"><span style="width:80%"></span></div>
  <div class="kicker">SITUATION 04/05</div>
  <h2 class="question">Wie fühlst du dich, wenn du nichts kaufst?</h2>
  <div class="option" style="top:268px;height:100px"><h3>Enttäuscht</h3><p>Mir fehlt das Belohnungsgefühl.</p>
    <svg width="16" height="16" viewBox="0 0 24 24" fill="none" stroke="currentColor" stroke-width="2" stroke-linecap="round"><circle cx="12" cy="12" r="9"/><path d="M9 16c2-2 4-2 6 0M9 10h.01M15 10h.01"/></svg></div>
  <div class="option" style="top:384px;height:99px"><h3>Stolz / Erleichtert</h3><p>Geld gespart für Wichtigeres.</p>
    <svg width="16" height="16" viewBox="0 0 24 24" fill="none" stroke="currentColor" stroke-width="2" stroke-linecap="round"><circle cx="12" cy="12" r="9"/><path d="M8 14c2 3 6 3 8 0M9 10h.01M15 10h.01"/></svg></div>
  <div class="option" style="top:500px;height:95px"><h3>Ist mir egal</h3><p>Es hat keine Bedeutung für mich.</p>
    <svg width="16" height="16" viewBox="0 0 24 24" fill="none" stroke="currentColor" stroke-width="2" stroke-linecap="round"><path d="M6 12h12"/></svg></div>
  <div class="next" style="top:697px"><svg width="18" height="18" viewBox="0 0 24 24" fill="none" stroke="currentColor" stroke-width="2.2" stroke-linecap="round"><path d="M5 12h14M13 6l6 6-6 6"/></svg></div>
</section>

<div class="screen-label" style="left:45px;top:1779px">7. Quiz Question 5</div>
<div class="screen-label" style="left:430px;top:1779px">8. Quiz Result</div>
<div class="screen-label" style="left:814px;top:1779px">9. Profile Detail</div>

<!-- 7 Quiz Q5 -->
<section class="phone" style="left:45px;top:1809px">
  <div class="progress"><span style="width:100%"></span></div>
  <div class="kicker">SITUATION 05/05</div>
  <h2 class="question">Was motiviert dich am meisten zum Sparen?</h2>
  <div class="option" style="top:272px;height:97px"><h3>Große Ziele</h3><p>Reisen, Haus oder Investitionen.</p>
    <svg width="16" height="16" viewBox="0 0 24 24" fill="none" stroke="currentColor" stroke-width="2" stroke-linejoin="round"><path d="M3 6l6-2 6 2 6-2v14l-6 2-6-2-6 2zM9 4v14M15 6v14"/></svg></div>
  <div class="option" style="top:386px;height:97px"><h3>Sicherheit</h3><p>Ein Polster für Notfälle.</p>
    <svg width="16" height="16" viewBox="0 0 24 24" fill="none" stroke="currentColor" stroke-width="2"><path d="M12 3l8 3v6c0 5-4 8-8 9-4-1-8-4-8-9V6z"/></svg></div>
  <div class="option" style="top:500px;height:97px"><h3>Mehr Freiheit</h3><p>Weniger Abhängigkeit von Geld.</p>
    <svg width="16" height="16" viewBox="0 0 24 24" fill="none" stroke="currentColor" stroke-width="2" stroke-linecap="round"><path d="M20 4C12 4 6 9 6 18M6 18l-2 2M6 14h7M9 10h8"/></svg></div>
  <div class="next" style="top:697px"><svg width="18" height="18" viewBox="0 0 24 24" fill="none" stroke="currentColor" stroke-width="2.2" stroke-linecap="round"><path d="M5 12h14M13 6l6 6-6 6"/></svg></div>
</section>

<!-- 8 Result -->
<section class="phone" style="left:430px;top:1809px;background:linear-gradient(180deg,#0a0a0a 0%,#0b0c0a 45%,#16230e 100%)">
  <div class="abs" style="left:90px;top:153px;width:149px;height:149px;border-radius:50%;background:#141414;border:1px solid #2a2a2a;display:flex;align-items:center;justify-content:center;color:var(--lime)">
    <svg width="56" height="56" viewBox="0 0 24 24" fill="none" stroke="currentColor" stroke-width="2" stroke-linejoin="round"><path d="M12 20s-8-5-8-11a4.5 4.5 0 018-2.8A4.5 4.5 0 0120 9c0 6-8 11-8 11z"/><path d="M8 11l3 2 4-4"/></svg>
  </div>
  <div class="abs center" style="top:342px;font-size:11px;letter-spacing:1.4px;color:var(--muted)">DEIN ERGEBNIS</div>
  <h1 class="abs center title" style="top:366px;font-size:33px;line-height:38px">Der emotionale<br>Ausgleicher</h1>
  <p class="abs center" style="top:455px;font-size:15.5px;line-height:27px;color:#9a9a9a;padding:0 36px">Du nutzt Einkäufe oft unbewusst, um für Balance in stressigen Zeiten zu sorgen.</p>
  <div class="btn btn-white" style="left:76px;width:185px;top:578px;font-size:14px;gap:8px">Mehr erfahren
    <svg width="12" height="12" viewBox="0 0 24 24" fill="none" stroke="currentColor" stroke-width="2.4" stroke-linecap="round"><path d="M6 9l6 6 6-6"/></svg></div>
</section>

<!-- 9 Profile -->
<section class="phone" style="left:814px;top:1809px;height:1096px">
  <div class="round-icon" style="left:33px;top:50px"><svg width="15" height="15" viewBox="0 0 24 24" fill="none" stroke="currentColor" stroke-width="2.2" stroke-linecap="round"><path d="M19 12H5M11 6l-6 6 6 6"/></svg></div>
  <div class="abs" style="left:85px;top:59px;font-size:16px;font-weight:500">Dein Profil</div>
  <h1 class="abs title" style="left:33px;top:116px;font-size:28px;line-height:34px">Der emotionale<br>Ausgleicher</h1>
  <div class="profile-card" style="top:204px;height:240px">
    <div class="badge" style="background:#282556;color:var(--purple)"><svg width="15" height="15" viewBox="0 0 24 24" fill="none" stroke="currentColor" stroke-width="2" stroke-linejoin="round"><path d="M13 3L5 14h6l-1 7 8-11h-6z"/></svg></div>
    <h3>Der Auslöser</h3>
    <p>Oft ist es nicht das Produkt selbst, sondern das Gefühl des "Sich-Gönnens" nach Anstrengung oder Stress, das dich zum Kaufen bewegt.</p>
  </div>
  <div class="profile-card" style="top:467px;height:217px">
    <div class="badge" style="background:#3a2515;color:#f0883e"><svg width="15" height="15" viewBox="0 0 24 24" fill="none" stroke="currentColor" stroke-width="2" stroke-linejoin="round"><path d="M12 4l9 16H3z"/><path d="M12 10v4M12 17h.01"/></svg></div>
    <h3>Die Falle</h3>
    <p>Kurzfristige Freude verwandelt sich schnell in Gleichgültigkeit gegenüber dem Gegenstand, sobald die Emotion abklingt.</p>
  </div>
  <div class="profile-card" style="top:709px;height:240px;background:linear-gradient(180deg,#1c2713,#141a0f);border-color:#34471e">
    <div class="badge" style="background:#2c3d18;color:var(--lime)"><svg width="15" height="15" viewBox="0 0 24 24" fill="none" stroke="currentColor" stroke-width="2" stroke-linecap="round"><circle cx="12" cy="12" r="3"/><path d="M12 3v2M12 19v2M3 12h2M19 12h2M5.6 5.6l1.4 1.4M17 17l1.4 1.4M5.6 18.4L7 17M17 7l1.4-1.4"/></svg></div>
    <h3 style="color:var(--lime)">Deine Superkraft</h3>
    <p style="color:#bbb">Du bist sehr reflektiert. Wenn du lernst, kurz innezuhalten, kannst du diese Energie in kreative oder entspannende Aktivitäten umlenken.</p>
  </div>
  <div class="btn btn-white" style="top:1005px;font-size:14px">Mein Dashboard öffnen</div>
</section>

<div class="screen-label" style="left:45px;top:2645px">10. Home Dashboard</div>
<div class="screen-label" style="left:430px;top:2645px">11. Statistics</div>

<!-- 10 Dashboard -->
<section class="phone" style="left:45px;top:2675px;height:800px">
  <div class="abs" style="left:33px;top:56px;font-size:11.5px;color:#999">Dienstag, 24. Okt</div>
  <div class="abs" style="left:33px;top:78px;font-size:21px;font-weight:500;letter-spacing:-.3px">Guten Morgen, Anna</div>
  <div class="abs" role="img" aria-label="Profilbild der Nutzerin" style="left:264px;top:69px;width:36px;height:36px;border-radius:50%;background:linear-gradient(135deg,#e8e2d6,#b9c9a4)"></div>
  <div class="abs" style="left:33px;top:132px;width:263px;height:245px;border-radius:18px;background:linear-gradient(160deg,#2b2660 0%,#1a1738 55%,#121021 100%);border:1px solid #2f2b5c;padding:22px 30px 22px 22px">
    <span style="display:inline-block;background:#4a3fb0;color:#d6d0ff;font-size:8.5px;font-weight:600;letter-spacing:1px;padding:4px 8px;border-radius:6px">DAILY INSIGHT</span>
    <p style="font-size:18px;line-height:27px;font-weight:500;margin-top:14px">"Nicht zu kaufen ist auch eine Einnahme."</p>
    <p style="font-size:11.5px;line-height:18px;color:#9c97c9;margin-top:10px">Überlege heute bei einer Ausgabe: Wie lange müsstest du dafür arbeiten?</p>
    <div style="font-size:12px;font-weight:500;margin-top:18px;display:flex;align-items:center;gap:8px">Gedanken notieren
      <svg width="12" height="12" viewBox="0 0 24 24" fill="none" stroke="currentColor" stroke-width="2.4" stroke-linecap="round"><path d="M5 12h14M13 6l6 6-6 6"/></svg></div>
  </div>
  <div class="stat-box" style="left:33px">
    <svg width="20" height="20" viewBox="0 0 24 24" fill="none" stroke="var(--lime)" stroke-width="2" stroke-linejoin="round"><path d="M4 14c0-5 5-8 12-8 2 0 3 1 3 2-2 0-3 1-3 3v4l-3 2H8z"/><path d="M8 17v3M14 17v3"/></svg>
    <strong>42€</strong><span>Diese Woche<br>gespart</span>
  </div>
  <div class="stat-box" style="left:173px">
    <svg width="20" height="20" viewBox="0 0 24 24" fill="none" stroke="#ff6b4a" stroke-width="2" stroke-linecap="round" stroke-linejoin="round"><path d="M3 12h4l3-8 4 16 3-8h4"/></svg>
    <strong>3</strong><span>Impulse<br>vermieden</span>
  </div>
  <div class="abs" style="left:33px;top:565px;font-size:15px;font-weight:500">Aktive Challenge</div>
  <div class="abs" style="left:33px;top:593px;width:263px;height:90px;border-radius:16px;background:var(--card);border:1px solid var(--card-line);display:flex;align-items:center;padding:0 14px;gap:16px">
    <div style="width:66px;height:62px;border-radius:12px;background:#0d0d0d;border:1px solid #222;display:flex;align-items:center;justify-content:center;color:var(--lime);font-size:22px;font-weight:600">04</div>
    <div style="flex:1">
      <div style="font-size:14px;font-weight:500">Newsletter Detox</div>
      <div style="height:4px;background:#2a2a2a;border-radius:2px;margin:9px 0 7px;width:100px"><div style="width:55%;height:4px;background:var(--lime);border-radius:2px"></div></div>
      <div style="font-size:10px;color:var(--dim)">Tag 4 von 10</div>
    </div>
  </div>
  <nav class="nav">
    <div class="nav-item active"><svg width="20" height="20" viewBox="0 0 24 24" fill="none" stroke="currentColor" stroke-width="2" stroke-linejoin="round"><path d="M3 11l9-7 9 7v9h-6v-6H9v6H3z"/></svg>Home</div>
    <div class="nav-item"><svg width="20" height="20" viewBox="0 0 24 24" fill="none" stroke="currentColor" stroke-width="2" stroke-linecap="round"><path d="M6 20v-6M12 20V5M18 20v-9"/></svg>Statistik</div>
    <div class="nav-item"><svg width="20" height="20" viewBox="0 0 24 24" fill="none" stroke="currentColor" stroke-width="2" stroke-linejoin="round"><path d="M12 3l9 5-9 5-9-5z"/><path d="M3 13l9 5 9-5"/></svg>Challenge</div>
    <div class="nav-item"><svg width="20" height="20" viewBox="0 0 24 24" fill="currentColor"><circle cx="5" cy="12" r="2"/><circle cx="12" cy="12" r="2"/><circle cx="19" cy="12" r="2"/></svg>Menü</div>
  </nav>
</section>

<!-- 11 Statistics -->
<section class="phone" style="left:430px;top:2675px;height:790px">
  <div class="abs" style="left:33px;top:55px;font-size:22px;font-weight:500;letter-spacing:-.3px">Deine Erfolge</div>
  <div class="abs" style="left:230px;top:52px;width:66px;height:26px;border-radius:13px;background:#1a1a1a;border:1px solid #2a2a2a;font-size:10.5px;color:#aaa;display:flex;align-items:center;justify-content:center">Oktober</div>
  <div class="abs center" style="top:143px;font-size:11.5px;color:var(--dim)">Durch bewusste Entscheidungen gespart</div>
  <div class="abs center" style="top:164px;font-size:44px;font-weight:600;letter-spacing:-1px">245€</div>
  <div class="abs center" style="top:225px;font-size:11.5px;color:var(--lime)">↗ +120€ zum Vormonat</div>
  <svg class="abs" style="left:0;top:260px" width="329" height="170" viewBox="0 0 329 170">
    <rect x="40" y="107" width="62" height="55" fill="#151515"/>
    <rect x="102" y="83" width="62" height="79" fill="#181818"/>
    <rect x="164" y="69" width="62" height="93" fill="#1a1a1a"/>
    <rect x="228" y="36" width="62" height="126" fill="#c5f25b"/>
    <rect x="228" y="6" width="62" height="22" rx="3" fill="#2a2a2a"/>
    <text x="259" y="21" fill="#ddd" font-family="Inter, sans-serif" font-size="10" text-anchor="middle">Woche 4</text>
  </svg>
  <div class="section-title" style="top:458px">ERFOLGE</div>
  <div class="win-card" style="top:488px;height:112px">
    <div class="badge" style="background:#282556;color:#a79cff"><svg width="16" height="16" viewBox="0 0 24 24" fill="none" stroke="currentColor" stroke-width="2"><circle cx="12" cy="12" r="8"/><path d="M7 7l10 10"/></svg></div>
    <h4>3x "Nein" gesagt</h4>
    <p>Du hast drei Impulskäufe in der Kategorie "Technik" vermieden.</p>
  </div>
  <div class="win-card" style="top:617px;height:100px;padding-right:60px">
    <div class="badge" style="background:#1b2b4a;color:#6fa2ff"><svg width="16" height="16" viewBox="0 0 24 24" fill="none" stroke="currentColor" stroke-width="2"><circle cx="12" cy="12" r="8"/><path d="M12 8v4l3 2"/></svg></div>
    <h4>24h Wartezeit eingehalten</h4>
    <p>Bei deinem Wunschzettel</p>
  </div>
  <nav class="nav">
    <div class="nav-item"><svg width="20" height="20" viewBox="0 0 24 24" fill="none" stroke="currentColor" stroke-width="2" stroke-linejoin="round"><path d="M3 11l9-7 9 7v9h-6v-6H9v6H3z"/></svg>Home</div>
    <div class="nav-item active"><svg width="20" height="20" viewBox="0 0 24 24" fill="none" stroke="currentColor" stroke-width="2" stroke-linecap="round"><path d="M6 20v-6M12 20V5M18 20v-9"/></svg>Statistik</div>
    <div class="nav-item"><svg width="20" height="20" viewBox="0 0 24 24" fill="none" stroke="currentColor" stroke-width="2" stroke-linejoin="round"><path d="M12 3l9 5-9 5-9-5z"/><path d="M3 13l9 5 9-5"/></svg>Challenge</div>
    <div class="nav-item"><svg width="20" height="20" viewBox="0 0 24 24" fill="currentColor"><circle cx="5" cy="12" r="2"/><circle cx="12" cy="12" r="2"/><circle cx="19" cy="12" r="2"/></svg>Menü</div>
  </nav>
</section>

<div class="screen-label" style="left:45px;top:3524px">13. Settings</div>
<div class="screen-label" style="left:446px;top:3503px">12. Challenge Details</div>

<!-- 13 Settings -->
<section class="phone" style="left:45px;top:3553px;height:790px">
  <h1 class="abs title" style="left:33px;top:52px;font-size:28px">Einstellungen</h1>
  <div class="section-title" style="top:117px">PRÄFERENZEN</div>
  <div class="group" style="top:137px">
    <div class="row">Mitteilungen<span class="toggle"></span></div>
    <div class="row">Daily Reminder Zeit<span class="meta">08:00</span></div>
  </div>
  <div class="section-title" style="top:281px">ACCOUNT &amp; DATEN</div>
  <div class="group" style="top:301px">
    <div class="row">Profil bearbeiten<svg width="12" height="12" viewBox="0 0 24 24" fill="none" stroke="currentColor" stroke-width="2.4" stroke-linecap="round"><path d="M9 6l6 6-6 6"/></svg></div>
    <div class="row">Exportiere meine Daten<svg width="14" height="14" viewBox="0 0 24 24" fill="none" stroke="currentColor" stroke-width="2" stroke-linecap="round"><path d="M12 4v11M7 10l5 5 5-5M4 20h16"/></svg></div>
    <div class="row">Privatsphäre<svg width="14" height="14" viewBox="0 0 24 24" fill="none" stroke="currentColor" stroke-width="2"><rect x="5" y="11" width="14" height="9" rx="2"/><path d="M8 11V8a4 4 0 018 0v3"/></svg></div>
  </div>
  <div class="section-title" style="top:499px">SUPPORT</div>
  <div class="group" style="top:519px">
    <div class="row">Hilfe &amp; FAQ<svg width="13" height="13" viewBox="0 0 24 24" fill="none" stroke="currentColor" stroke-width="2" stroke-linecap="round"><path d="M14 4h6v6M20 4l-9 9M18 14v6H4V6h6"/></svg></div>
  </div>
  <div class="abs center" style="top:634px;font-size:13px;color:var(--danger)">Abmelden</div>
  <div class="abs center" style="top:679px;font-size:9px;color:#444">Version 1.0.2 • Build 2490</div>
  <nav class="nav">
    <div class="nav-item"><svg width="20" height="20" viewBox="0 0 24 24" fill="none" stroke="currentColor" stroke-width="2" stroke-linejoin="round"><path d="M3 11l9-7 9 7v9h-6v-6H9v6H3z"/></svg>Home</div>
    <div class="nav-item"><svg width="20" height="20" viewBox="0 0 24 24" fill="none" stroke="currentColor" stroke-width="2" stroke-linecap="round"><path d="M6 20v-6M12 20V5M18 20v-9"/></svg>Statistik</div>
    <div class="nav-item"><svg width="20" height="20" viewBox="0 0 24 24" fill="none" stroke="currentColor" stroke-width="2" stroke-linejoin="round"><path d="M12 3l9 5-9 5-9-5z"/><path d="M3 13l9 5 9-5"/></svg>Challenge</div>
    <div class="nav-item active"><svg width="20" height="20" viewBox="0 0 24 24" fill="currentColor"><circle cx="5" cy="12" r="2"/><circle cx="12" cy="12" r="2"/><circle cx="19" cy="12" r="2"/></svg>Menü</div>
  </nav>
</section>

<!-- 12 Challenge detail -->
<section class="phone" style="left:446px;top:3532px;height:790px">
  <div class="round-icon" style="left:32px;top:50px"><svg width="15" height="15" viewBox="0 0 24 24" fill="none" stroke="currentColor" stroke-width="2.2" stroke-linecap="round"><path d="M19 12H5M11 6l-6 6 6 6"/></svg></div>
  <svg class="abs" style="left:275px;top:60px;color:#ccc" width="17" height="17" viewBox="0 0 24 24" fill="none" stroke="currentColor" stroke-width="2"><circle cx="18" cy="5" r="3"/><circle cx="6" cy="12" r="3"/><circle cx="18" cy="19" r="3"/><path d="M8.6 10.5l6.8-4M8.6 13.5l6.8 4"/></svg>
  <div class="abs" style="left:117px;top:119px;width:98px;height:20px;border-radius:10px;background:#1e2a12;border:1px solid #3a5220;color:var(--lime);font-size:10px;font-weight:700;letter-spacing:1px;display:flex;align-items:center;justify-content:center">CHALLENGE</div>
  <h1 class="abs center title" style="top:150px;font-size:29px;line-height:35px">10 Tage<br>Aussortieren</h1>
  <p class="abs center" style="top:232px;font-size:14px;line-height:22px;color:#9a9a9a;padding:0 38px">Schaffe Raum für Neues, indem du Altes loslässt.</p>
  <div class="abs" style="left:33px;top:298px;width:263px;height:271px;border-radius:22px;background:#141414;border:1px solid #262626;text-align:center;padding-top:24px">
    <div style="width:42px;height:42px;border-radius:50%;background:var(--lime);color:#0a0a0a;font-size:14px;font-weight:700;display:flex;align-items:center;justify-content:center;margin:0 auto">01</div>
    <div style="font-size:18px;font-weight:500;margin-top:21px">Der Kleiderschrank</div>
    <p style="font-size:12px;line-height:21px;color:#8a8a8a;margin:10px 24px 0">Finde 3 Teile, die du seit einem Jahr nicht getragen hast. Spende oder verkaufe sie heute.</p>
    <div style="margin:18px auto 0;width:218px;height:46px;border-radius:12px;background:#fff;color:#0a0a0a;font-size:13px;font-weight:500;display:flex;align-items:center;justify-content:center;gap:8px">
      <svg width="14" height="14" viewBox="0 0 24 24" fill="none" stroke="currentColor" stroke-width="2.2" stroke-linecap="round"><circle cx="12" cy="12" r="9"/><path d="M8 12l3 3 5-6"/></svg>Als erledigt markieren</div>
  </div>
  <div class="step" style="top:610px">Tag 02: Digitale Abos prüfen</div>
  <div class="step" style="top:647px">Tag 03: Vorratskammer leeren</div>
  <div class="step" style="top:685px">Tag 04: Badezimmer Check</div>
  <nav class="nav">
    <div class="nav-item"><svg width="20" height="20" viewBox="0 0 24 24" fill="none" stroke="currentColor" stroke-width="2" stroke-linejoin="round"><path d="M3 11l9-7 9 7v9h-6v-6H9v6H3z"/></svg>Home</div>
    <div class="nav-item"><svg width="20" height="20" viewBox="0 0 24 24" fill="none" stroke="currentColor" stroke-width="2" stroke-linecap="round"><path d="M6 20v-6M12 20V5M18 20v-9"/></svg>Statistik</div>
    <div class="nav-item active"><svg width="20" height="20" viewBox="0 0 24 24" fill="none" stroke="currentColor" stroke-width="2" stroke-linejoin="round"><path d="M12 3l9 5-9 5-9-5z"/><path d="M3 13l9 5 9-5"/></svg>Challenge</div>
    <div class="nav-item"><svg width="20" height="20" viewBox="0 0 24 24" fill="currentColor"><circle cx="5" cy="12" r="2"/><circle cx="12" cy="12" r="2"/><circle cx="19" cy="12" r="2"/></svg>Menü</div>
  </nav>
</section>

</body>
</html>
```